LA's Newest VERDA Facial Oil and Body Oil Packaging Project

We need a packaging concept for a verda based facial oil and body oil. We need label design for the bottle and carton graphics. I am attaching a few reference photos. The target demographic is women between 17-35 year old. Products need to be able to stand out in crowded stores with clear calls to action.
1oz Dropper Bottle with Unit Carton - verda Facial Oil
4oz PET Bottle with Unit Carton - verda + Rose Facial Oil

```html
<!DOCTYPE html>
<html lang="en">
<head>
<meta charset="utf-8">
<title>Verda Facial Oil – Packaging Graphics</title>
<link rel="stylesheet" href="https://fonts.googleapis.com/css2?family=Raleway:wght@300;400&family=Roboto+Condensed:wght@300;400&display=swap">
<style>
  :root {
    --ink: #0d0d0d;
    --paper: #ffffff;
    --panel-white: #f4f4f4;
    --gold-light: #f3dc8a;
    --gold: #d4a935;
    --gold-deep: #9c7418;
    --grey-text: #555555;
    --rose: #e9b6cf;
    --leafy: #a9cdb8;
    --sky: #b9cfe8;
  }
  * { margin: 0; padding: 0; box-sizing: border-box; }
  html, body { width: 1200px; height: 1071px; overflow: hidden; background: var(--paper); }
  .stage { position: relative; width: 1200px; height: 1071px; }

  .panel {
    position: absolute;
    background: var(--panel-white);
    overflow: hidden;
    box-shadow: 0 2px 10px rgba(0,0,0,0.12);
  }
  .panel__dark {
    position: absolute; left: 0; top: 0; right: 0;
    background: var(--ink);
  }
  .panel__wave { position: absolute; left: 0; width: 100%; display: block; }

  .wordmark {
    position: absolute; left: 0; right: 0; text-align: center;
    font-family: "Raleway", sans-serif; font-weight: 300;
    color: var(--paper); letter-spacing: -1px; line-height: 1;
  }
  .variant-tag {
    position: absolute; left: 50%; transform: translateX(-50%);
    white-space: nowrap;
    font-family: "Roboto Condensed", sans-serif; font-weight: 400;
    color: var(--ink); letter-spacing: 1px;
    background: linear-gradient(90deg, var(--gold-deep), var(--gold-light) 45%, var(--gold) 100%);
    padding: 3px 10px;
  }
  .variant-tag--rose { letter-spacing: 0; }
  .leaf-emblem {
    position: absolute; left: 50%; transform: translateX(-50%);
    border-radius: 50% 50% 10% 10%;
    background: radial-gradient(circle at 50% 40%, var(--gold-light), var(--gold) 55%, var(--gold-deep));
  }
  .floral-band {
    position: absolute; left: 0; right: 0;
    background: linear-gradient(90deg, var(--rose), var(--sky) 30%, var(--leafy) 50%, var(--rose) 75%, var(--sky));
    opacity: 0.75;
  }
  .skin-line, .volume {
    position: absolute; left: 0; right: 0; text-align: center;
    font-family: "Roboto Condensed", sans-serif; font-weight: 300;
    color: var(--grey-text); white-space: nowrap;
  }
  .skin-line--on-dark { color: #9a9a9a; }
  .mini-mark {
    position: absolute;
    font-family: "Raleway", sans-serif; font-weight: 300;
    color: var(--grey-text); line-height: 1;
  }
  .mini-mark small {
    display: block; font-family: "Roboto Condensed", sans-serif;
    font-size: 10px; letter-spacing: 1px; margin-top: 2px;
  }
</style>
</head>
<body>
<main class="stage">

  <!-- 1 oz carton front -->
  <section class="panel carton carton--facial" style="left:80px; top:300px; width:220px; height:520px;">
    <div class="panel__dark" style="height:360px;"></div>
    <svg class="panel__wave" style="top:330px;" viewBox="0 0 220 70" height="70" preserveAspectRatio="none">
      <path d="M0 0 H220 V20 C150 10 80 60 0 40 Z" fill="#0d0d0d"/>
      <path d="M0 40 C80 60 150 10 220 20 V27 C150 18 80 68 0 47 Z" fill="#d4a935"/>
    </svg>
    <div class="wordmark" style="top:70px; font-size:60px;">verda</div>
    <div class="variant-tag" style="top:150px; font-size:16px;">FACIAL OIL</div>
    <div class="leaf-emblem" role="img" aria-label="Gold leaf emblem" style="top:205px; width:90px; height:90px;"></div>
    <div class="mini-mark" style="left:14px; top:420px; font-size:24px;">verda<small>FACIAL OIL</small></div>
    <div class="skin-line" style="top:432px; left:92px; font-size:14px;">For All Skin Types</div>
    <div class="volume" style="top:488px; font-size:13px;">1 oz / 30 ml</div>
  </section>

  <!-- 1 oz dropper bottle label -->
  <section class="panel label label--dropper" style="left:350px; top:520px; width:190px; height:300px;">
    <div class="panel__dark" style="height:200px;"></div>
    <svg class="panel__wave" style="top:180px;" viewBox="0 0 190 50" height="50" preserveAspectRatio="none">
      <path d="M0 0 H190 V14 C130 6 70 44 0 28 Z" fill="#0d0d0d"/>
      <path d="M0 28 C70 44 130 6 190 14 V20 C130 12 70 50 0 34 Z" fill="#d4a935"/>
    </svg>
    <div class="wordmark" style="top:30px; font-size:46px;">verda</div>
    <div class="variant-tag" style="top:94px; font-size:13px;">FACIAL OIL</div>
    <div class="leaf-emblem" role="img" aria-label="Gold leaf emblem" style="top:128px; width:56px; height:56px;"></div>
    <div class="skin-line" style="top:236px; font-size:10px;">For All Skin Types</div>
    <div class="volume" style="top:262px; font-size:13px;">1 oz / 30 ml</div>
  </section>

  <!-- 4 oz PET bottle label -->
  <section class="panel label label--pet" style="left:590px; top:400px; width:200px; height:420px;">
    <div class="panel__dark" style="height:290px;"></div>
    <svg class="panel__wave" style="top:270px;" viewBox="0 0 200 50" height="50" preserveAspectRatio="none">
      <path d="M0 0 H200 V14 C140 6 70 44 0 28 Z" fill="#0d0d0d"/>
      <path d="M0 28 C70 44 140 6 200 14 V20 C140 12 70 50 0 34 Z" fill="#d4a935"/>
    </svg>
    <div class="wordmark" style="top:40px; font-size:52px;">verda</div>
    <div class="variant-tag variant-tag--rose" style="top:110px; font-size:14px;">+ Rose Facial Oil</div>
    <div class="skin-line skin-line--on-dark" style="top:146px; font-size:11px;">For All Skin Types</div>
    <div class="leaf-emblem" role="img" aria-label="Gold leaf emblem" style="top:190px; width:64px; height:64px;"></div>
    <div class="floral-band" role="img" aria-label="Watercolour rose and foliage border" style="top:300px; height:60px;"></div>
    <div class="volume" style="top:384px; font-size:12px;">4 oz / 118 ml</div>
  </section>

  <!-- 4 oz carton front -->
  <section class="panel carton carton--rose" style="left:840px; top:220px; width:260px; height:600px;">
    <div class="panel__dark" style="height:410px;"></div>
    <svg class="panel__wave" style="top:380px;" viewBox="0 0 260 70" height="70" preserveAspectRatio="none">
      <path d="M0 0 H260 V20 C180 10 90 60 0 40 Z" fill="#0d0d0d"/>
      <path d="M0 40 C90 60 180 10 260 20 V27 C180 18 90 68 0 47 Z" fill="#d4a935"/>
    </svg>
    <div class="wordmark" style="top:90px; font-size:66px;">verda</div>
    <div class="variant-tag variant-tag--rose" style="top:178px; font-size:16px;">+ Rose Facial Oil</div>
    <div class="leaf-emblem" role="img" aria-label="Gold leaf emblem" style="top:250px; width:100px; height:100px;"></div>
    <div class="floral-band" role="img" aria-label="Watercolour rose and foliage border" style="top:420px; height:70px;"></div>
    <div class="skin-line" style="top:508px; font-size:16px;">For All Skin Types</div>
    <div class="volume" style="top:558px; font-size:16px;">4 oz / 118 ml</div>
  </section>

</main>
</body>
</html>
```